Freshen up Product Labels

We need product label designs refreshed throughout our brand. We will start with the main product as that will set the basic design for most other labels. We are currently using 2.5" wide x 4.5" tall vinyl labels for most products and would like to stick to that size for this project. There are 3 of this size label on a jug of our all natural house cleaning concentrate. Uploaded current design and open to your new ideas. Our products can be found in more detail at quillbrook.com

```html
<!DOCTYPE html>
<html lang="en">
<head>
<meta charset="utf-8">
<title>Quillbrook Aromatherapy Cleaning Concentrate Label</title>
<link rel="stylesheet" href="https://fonts.googleapis.com/css2?family=Almendra:wght@700&family=Montserrat:wght@500;600;700&family=Rokkitt:wght@500&display=swap">
<style>
  :root {
    --maroon: #5c2a38;
    --leaf-green: #a9c748;
    --label-white: #ffffff;
    --backdrop: #e4e4e4;
    --faint-leaf: #e9e9e9;
  }
  * { margin: 0; padding: 0; box-sizing: border-box; }
  html, body {
    width: 1200px;
    height: 750px;
    overflow: hidden;
    background: var(--backdrop);
  }
  .label {
    position: absolute;
    left: 75px;
    top: 82px;
    width: 1050px;
    height: 585px;
    background: var(--label-white);
    overflow: hidden;
    font-family: "Montserrat", sans-serif;
  }
  .label-panels {
    position: absolute;
    inset: 0;
  }
  .oil-panel {
    position: absolute;
    left: 0;
    top: 0;
    width: 230px;
    height: 585px;
    text-align: center;
    color: var(--label-white);
  }
  .oil-intro {
    position: absolute;
    top: 140px;
    width: 100%;
    font-family: "Rokkitt", serif;
    font-weight: 500;
    font-size: 21px;
    line-height: 32px;
    letter-spacing: 1.5px;
  }
  .oil-list {
    position: absolute;
    top: 244px;
    width: 100%;
    list-style: none;
    color: var(--leaf-green);
    font-weight: 700;
    font-size: 22px;
    line-height: 38px;
    letter-spacing: 0.5px;
  }
  .formula-note {
    position: absolute;
    top: 490px;
    width: 100%;
    font-weight: 700;
    font-size: 18px;
    line-height: 32px;
  }
  .center-panel {
    position: absolute;
    left: 230px;
    top: 0;
    width: 585px;
    height: 585px;
    text-align: center;
  }
  .leaf-backdrop {
    position: absolute;
    left: 150px;
    top: 270px;
    width: 290px;
    height: 300px;
    border-radius: 50%;
    background: radial-gradient(ellipse at center, var(--faint-leaf) 0%, rgba(233,233,233,0.5) 50%, rgba(255,255,255,0) 72%);
  }
  .brand-name {
    position: absolute;
    top: 148px;
    left: 0;
    width: 100%;
    display: flex;
    justify-content: center;
    align-items: center;
    gap: 14px;
    color: var(--leaf-green);
    font-weight: 600;
    font-size: 50px;
    letter-spacing: 2px;
  }
  .brand-dot {
    width: 22px;
    height: 22px;
    border-radius: 50%;
    background: var(--leaf-green);
  }
  .product-title {
    position: absolute;
    top: 296px;
    width: 100%;
    color: var(--maroon);
    font-family: "Almendra", serif;
    font-weight: 700;
    font-size: 60px;
    line-height: 66px;
  }
  .site-address {
    position: absolute;
    top: 548px;
    width: 100%;
    color: var(--leaf-green);
    font-weight: 600;
    font-size: 15px;
    letter-spacing: 3px;
  }
  .yield-panel {
    position: absolute;
    left: 815px;
    top: 0;
    width: 235px;
    height: 585px;
    color: var(--label-white);
    text-align: center;
  }
  .yield-note {
    position: absolute;
    top: 262px;
    left: 30px;
    width: 190px;
    font-weight: 500;
    font-size: 22px;
    line-height: 27px;
  }
  .yield-icon {
    position: absolute;
    left: 20px;
    top: 258px;
  }
  .size-badge {
    position: absolute;
    left: 85px;
    top: 488px;
    width: 64px;
    height: 64px;
    border-radius: 50%;
    background: var(--label-white);
    color: var(--maroon);
    font-weight: 700;
    font-size: 20px;
    line-height: 64px;
  }
</style>
</head>
<body>
  <main class="label">
    <svg class="label-panels" width="1050" height="585" viewBox="0 0 1050 585" aria-hidden="true">
      <rect x="0" y="0" width="230" height="160" fill="var(--leaf-green)"/>
      <path d="M0,585 V150 A175,150 0 0 1 175,0 H230 V585 Z" fill="var(--maroon)"/>
      <path d="M815,0 H915 A135,155 0 0 1 1050,155 V585 H815 Z" fill="var(--maroon)"/>
    </svg>

    <section class="oil-panel">
      <p class="oil-intro">Contains<br>Powerful<br>Essential Oils</p>
      <ul class="oil-list">
        <li>·cinnamon·</li>
        <li>·clove·</li>
        <li>·lemon·</li>
        <li>·resemary·</li>
        <li>·peppermint·</li>
        <li>·eucalyptus·</li>
      </ul>
      <p class="formula-note">Ultra-Concentrated<br>Vesatile Formula</p>
    </section>

    <section class="center-panel">
      <div class="leaf-backdrop" role="img" aria-label="Faint scattered leaf decoration behind the product name"></div>
      <div class="brand-name"><span class="brand-dot"></span>QUILLBROOK</div>
      <h1 class="product-title">Aromatherapy<br>Cleaning<br>Concentrate</h1>
      <p class="site-address">QUILLBROOK.COM</p>
    </section>

    <section class="yield-panel">
      <svg class="yield-icon" width="30" height="26" viewBox="0 0 30 26" aria-hidden="true">
        <circle cx="8" cy="6" r="4" fill="var(--label-white)"/>
        <circle cx="19" cy="5" r="3" fill="var(--label-white)"/>
        <circle cx="6" cy="17" r="3" fill="var(--label-white)"/>
        <circle cx="16" cy="15" r="4" fill="var(--label-white)"/>
      </svg>
      <p class="yield-note">Makes up<br>to 24<br>Gallons<br>of<br>Cleaner</p>
      <div class="size-badge">64oz</div>
    </section>
  </main>
</body>
</html>
```